Business card design for Kovantrix

I need a business card based on the logo design produced for Kovantrix. The company is focused on triathlon and endurance sport coaching and the tag line is (per the logo) "Endurance. Resilience. Achievement". The design should be sophisticated, appropriate to an affluent and business oriented target market. Colors are optional but the color of the logo probably dictates the color used on the card. I envisage using the red logo, with black print for the wording and contact numbers on a white or cream background, but am open to alternative suggestions. I expect to select something fairly conventional, but would like to see some designs that are less conventional to stretch my thinking on what could be appropriate. I am assuming a single side design is best, but willing to consider double sided as an option.

Target Market(s)

Individual athletes and corporate health and wellness leaders

Industry/Entity Type

Health And Wellness

Contact Information for Business Card

The card should provide the following information:
Logo
My name: Marcus Bellingham
Company website: Kovantrix.com
My email: marcus.bellingham@kovantrix.com
My cell phone number: +1-555-812-6093

Font styles to use
Sans Serif

Colors

Designer to choose colors to be used in the design.

Requirements
Must have
• Space on the card - simple design, not over crowded.
Nice to have
• clean and clear font, nothing garish or mass market like
Should not have
• Do not add pictures

```html
<!DOCTYPE html>
<html lang="en">
<head>
<meta charset="utf-8">
<title>Kovantrix Business Card</title>
<link rel="stylesheet" href="https://fonts.googleapis.com/css2?family=Open+Sans:wght@400;700&family=Oswald:wght@600&display=swap">
<style>
  :root {
    --bg: #e6e6e6;
    --card: #ffffff;
    --card-shade: #f1f1f1;
    --brand-red: #a51d22;
    --ink: #2a2a2a;
  }
  * { margin: 0; padding: 0; box-sizing: border-box; }
  html, body { width: 1200px; height: 904px; overflow: hidden; }
  body {
    background: var(--bg);
    font-family: "Open Sans", Arial, sans-serif;
    position: relative;
  }
  .card {
    position: absolute;
    width: 580px;
    height: 331px;
    background: linear-gradient(135deg, var(--card) 0%, var(--card-shade) 100%);
    box-shadow: 0 10px 28px rgba(0,0,0,0.18);
    overflow: hidden;
  }
  .card--front { left: 70px; top: 80px; }
  .card--back { left: 550px; top: 490px; }

  .brand {
    position: absolute;
    color: var(--brand-red);
    font-weight: 700;
    font-size: 44px;
    line-height: 1;
    letter-spacing: -0.5px;
    white-space: nowrap;
  }
  .card--front .brand { left: 50%; top: 50%; transform: translate(-50%, -50%); }
  .card--back .brand { left: 38px; top: 92px; }

  .holder {
    position: absolute;
    right: 36px;
    top: 46px;
    font-family: "Oswald", "Arial Narrow", sans-serif;
    font-weight: 600;
    font-size: 26px;
    line-height: 1.3;
    color: var(--brand-red);
    text-transform: uppercase;
    letter-spacing: 0.3px;
    white-space: nowrap;
  }
  .holder-tab {
    position: absolute;
    right: 0;
    top: 40px;
    width: 18px;
    height: 46px;
    background: var(--brand-red);
  }

  .contact {
    position: absolute;
    left: 40px;
    bottom: 48px;
    list-style: none;
  }
  .contact__item {
    display: flex;
    align-items: center;
    gap: 12px;
    color: var(--ink);
    font-size: 15px;
    line-height: 25px;
  }
  .contact__icon { width: 16px; height: 16px; flex: none; }

  .base-band {
    position: absolute;
    left: 0; right: 0; bottom: 0;
    height: 16px;
    background: var(--brand-red);
  }
</style>
</head>
<body>

<section class="card card--front" aria-label="Card front">
  <span class="brand">Kovantrix</span>
</section>

<section class="card card--back" aria-label="Card back">
  <span class="brand">Kovantrix</span>

  <div class="holder-tab"></div>
  <h1 class="holder">Marcus Bellingham</h1>

  <ul class="contact">
    <li class="contact__item">
      <svg class="contact__icon" viewBox="0 0 16 16" aria-hidden="true">
        <circle cx="8" cy="8" r="8" fill="#a51d22"/>
        <path d="M5.2 4.2l1.4-.2.8 1.9-.9.7c.4.9 1.1 1.6 2 2l.7-.9 1.9.8-.2 1.4c-3 .3-6-2.7-5.7-5.7z" fill="#fff"/>
      </svg>
      +1-555-812-6093
    </li>
    <li class="contact__item">
      <svg class="contact__icon" viewBox="0 0 16 16" aria-hidden="true">
        <circle cx="8" cy="8" r="8" fill="#a51d22"/>
        <rect x="4" y="5.2" width="8" height="5.6" fill="none" stroke="#fff" stroke-width="1.1"/>
        <path d="M4 5.4l4 3 4-3" fill="none" stroke="#fff" stroke-width="1.1"/>
      </svg>
      marcus.bellingham@kovantrix.com
    </li>
    <li class="contact__item">
      <svg class="contact__icon" viewBox="0 0 16 16" aria-hidden="true">
        <circle cx="8" cy="8" r="8" fill="#a51d22"/>
        <circle cx="8" cy="8" r="4.2" fill="none" stroke="#fff" stroke-width="1"/>
        <ellipse cx="8" cy="8" rx="1.8" ry="4.2" fill="none" stroke="#fff" stroke-width="1"/>
        <path d="M3.8 8h8.4" stroke="#fff" stroke-width="1"/>
      </svg>
      www.Kovantrix.com
    </li>
  </ul>

  <div class="base-band"></div>
</section>

</body>
</html>
```